Verpackungsdesign für hochwertiges Haarparfum
Zielgruppe
Tovel's Method ist eine israelische Firma, die hochqualitative Haarprodukte und Haar Tools verkauft. Unsere Zielgruppe sind Frauen, die viel in Ihr Aussehen investieren und auf Ihr Äußeres sehr Wert legen.
Aufgabenstellung
Wir suchen nach einem Design für unsere zwei neuen Haarparfums. Es sollte teuer aussehen und das Design sollte modern und simpel sein. Die Flachen sind mit Milchglas und das Design wird auf die Flaschen gedruckt. Das Design muss komplett in Englischer Sprache sein.
Die Masse sind:
Höhe 7,7 cm
Umfang 11 cm
Es wird zwei Düfte geben.
1. The Nordic : Deckel wird Silber glänzend
2. The Celtic: Deckel wird Silber matt
Informationen die auf der Flasche sein sollten:
1. Firmen Logo (wird angehängt)
2. Name des Parfüms (The Nordic or the Celtic)
3. Longlasting Hair Fragrance
4. 30 ml
5. Includes essential hair vitamins and minerals
6. Alcohol and salt free

```html
<!DOCTYPE html>
<html lang="en">
<head>
<meta charset="utf-8">
<title>Tovel's Method – Nordic Hair Fragrance Label</title>
<link rel="stylesheet" href="https://fonts.googleapis.com/css2?family=Cinzel:wght@700&family=PT+Sans:wght@400;700&family=PT+Sans+Narrow:wght@400&display=swap">
<style>
  :root {
    --bg-top: #0d0c0b;
    --bg-bottom: #86684a;
    --label-left: #4a403a;
    --label-right: #857261;
    --ink: #ffffff;
    --bronze: #b08a67;
    --bronze-light: #e3d3c1;
    --logo-ink: #9c7a5c;
  }
  * { margin: 0; padding: 0; box-sizing: border-box; }
  html, body { width: 1200px; height: 1200px; overflow: hidden; }
  body {
    background: linear-gradient(160deg, var(--bg-top) 0%, #2e241d 40%, var(--bg-bottom) 100%);
    font-family: "PT Sans", sans-serif;
    color: var(--ink);
    position: relative;
  }
  .label {
    position: absolute;
    left: 60px; top: 330px;
    width: 1080px; height: 540px;
    background: linear-gradient(135deg, var(--label-left), var(--label-right));
  }
  .key-band {
    position: absolute;
    left: 6px; right: 6px; top: 120px; height: 54px;
    border-top: 2px solid var(--bronze-light);
    border-bottom: 2px solid var(--bronze-light);
  }
  .key-band .pattern {
    position: absolute; left: 0; right: 0; top: 8px; bottom: 8px;
    background: linear-gradient(90deg, #cbb49c, #8f6a4b 35%, #e9ddd0 60%, #9b7656 85%, #d8c3ad);
    opacity: 0.85;
  }
  .panel {
    position: absolute; top: 0; bottom: 0;
    display: flex; flex-direction: column; align-items: center;
    text-align: center;
  }
  .panel-back { left: 110px; width: 300px; }
  .panel-front { left: 640px; width: 340px; }

  .brand-mark {
    display: flex; align-items: center; gap: 8px;
    font-family: "PT Sans", sans-serif; font-weight: 400;
    letter-spacing: 0.18em; text-transform: uppercase;
  }
  .brand-mark .square { display: inline-block; border: 1.5px solid currentColor; }
  .panel-back .brand-mark { margin-top: 40px; font-size: 14px; color: var(--ink); }
  .panel-back .brand-mark .square { width: 14px; height: 14px; }

  .front-logo {
    margin-top: 20px;
    width: 200px; height: 200px;
    background: #ffffff;
    display: flex; align-items: center; justify-content: center;
  }
  .front-logo .brand-mark { font-size: 17px; color: var(--logo-ink); }
  .front-logo .square { width: 16px; height: 16px; }

  .scent-name {
    font-family: "Cinzel", serif; font-weight: 700;
    letter-spacing: 0.04em;
  }
  .panel-back .scent-name { margin-top: 176px; font-size: 20px; }
  .panel-front .scent-name { margin-top: 24px; font-size: 44px; }

  .product-type { line-height: 1.15; }
  .product-type .light { display: block; font-weight: 400; }
  .product-type .bold { display: block; font-weight: 700; }
  .panel-back .product-type { margin-top: 22px; font-size: 17px; }
  .panel-front .product-type { margin-top: 16px; font-size: 22px; font-family: "PT Sans Narrow", sans-serif; }
  .panel-front .product-type .bold { font-family: "PT Sans", sans-serif; font-size: 21px; }

  .rule { height: 1.5px; background: var(--bronze); }
  .panel-back .rule { width: 150px; margin-top: 12px; }
  .panel-front .rule { width: 240px; margin-top: 12px; }

  .ingredients { margin-top: 14px; font-size: 12px; line-height: 1.1; width: 160px; }
  .ingredients h3 { font-size: 13px; font-weight: 700; }

  .claims {
    margin-top: 12px;
    font-family: "PT Sans Narrow", sans-serif;
    font-size: 19px; line-height: 1.15;
  }
  .volume { margin-top: 16px; font-family: "PT Sans Narrow", sans-serif; font-size: 24px; }
</style>
</head>
<body>
  <section class="label">
    <div class="key-band">
      <div class="pattern" role="img" aria-label="Bronze Greek-key meander ornament running across the label"></div>
    </div>

    <div class="panel panel-back">
      <div class="brand-mark"><span class="square"></span>Tovel's Method</div>
      <h2 class="scent-name">NORDIC</h2>
      <p class="product-type"><span class="light">LONGLASTING</span><span class="bold">HAIR FRAGRANCE</span></p>
      <div class="rule"></div>
      <div class="ingredients">
        <h3>INGREDIENTS:</h3>
        <p>Lorem ipsum dolor sit amet, consectetur adipiscing elit, sed do eiusmod tempor incididunt ut labore et dolore magna aliqua. Ut enim ad minim veniam, quis nostrud exercitation ullamco laboris nisi ut aliquip ex ea commodo consequat</p>
      </div>
    </div>

    <div class="panel panel-front">
      <div class="front-logo">
        <div class="brand-mark"><span class="square"></span>Tovel's Method</div>
      </div>
      <h1 class="scent-name">NORDIC</h1>
      <p class="product-type"><span class="light">LONGLASTING</span><span class="bold">HAIR FRAGRANCE</span></p>
      <div class="rule"></div>
      <p class="claims">Includes essential hair<br>vitamins and minerals<br>Alcohol and salt free</p>
      <p class="volume">30 ml</p>
    </div>
  </section>
</body>
</html>
```